DERMATOLOGY SERVICES ADDING CARE FOR sKIN, HAIR AND NAILS

postcard TO BE DISTRIBUTED TO RURAL COMMUNITY. medical CLINIC EXPANDING AND ADDING DERMATOLOGIST. TREATMENT OF skin PROBLEMS LIKE RASHES, SABIES, SKIN CANCERS, ROSACEA, PSORIASIS, ECZEMA, WOUND CARE, ACNE, ANTI-AGING AND OTHER BREAKDOWN OF SKIN.
SERVICES INCLUDED PLEASE SEE ATTACHED DOCUMENT
Updates

Project Deadline Extended
Reason: The designs we got few designers that sent designs and they are not what we want. We need to have more time

Target Market(s)

rural COMMUNITY

Industry/Entity Type

Medical

Font styles to use
Other font styles liked:
• LET DESIGNER CHOOSE

Requirements
Must have
• SKIN PROBLEMS AND DISORDERS MENTIONED IN THE ATTACHED FILES
• MEDICAL PROFESSION
• ADDRESS PHONE NUMBERS
• 482 N Larkin Avenue Wauchula, Florida 33870
• phone # 863-555-0182
• Marlow Tenbury Inc expanding its services
• mOST INSURANCE ACCEPTED INCLUDING MEDICARE
Nice to have
• ADD A LOGO
Should not have
• This is a US postcard to be left in restaurants, doctors offices RV park. No stamp or address line in the back

```html
<!DOCTYPE html>
<html lang="en">
<head>
<meta charset="utf-8">
<title>Dermatology Services Postcard</title>
<link href="https://fonts.googleapis.com/css2?family=Oswald:wght@400;500;600&family=Open+Sans:wght@400;600;700&family=Berkshire+Swash&display=swap" rel="stylesheet">
<style>
  :root {
    --page-bg: #ececec;
    --card-bg: #ffffff;
    --orange: #e07f3c;
    --pink: #f0b6c0;
    --pink-deep: #e48ea0;
    --pink-soft: #f8dde2;
    --brown: #7b5646;
    --tan: #c6937a;
    --ink: #2b2b2b;
    --muted: #6b6b6b;
    --skin-light: #f3dccd;
    --skin-mid: #ddb49c;
  }
  * { box-sizing: border-box; margin: 0; padding: 0; }
  html, body { width: 900px; height: 1200px; overflow: hidden; }
  body { background: var(--page-bg); position: relative; font-family: "Open Sans", sans-serif; }

  .postcard {
    position: absolute; left: 40px; width: 820px; height: 540px;
    background: var(--card-bg); overflow: hidden;
    box-shadow: 0 6px 18px rgba(0,0,0,.18);
  }
  .postcard--front { top: 45px; }
  .postcard--back { top: 615px; }

  /* Front */
  .headline {
    position: absolute; left: 32px; top: 28px; width: 390px;
    font-family: "Oswald", sans-serif; font-weight: 600; font-size: 27px;
    line-height: 1.15; color: var(--orange); text-transform: uppercase;
  }
  .hero-photo {
    position: absolute; right: 0; top: 0; width: 420px; height: 360px;
    background: radial-gradient(ellipse at 55% 40%, var(--skin-light), var(--skin-mid) 70%, #b98a73);
  }
  .circle-photo {
    position: absolute; border-radius: 50%; border: 5px solid #fff;
    box-shadow: 0 2px 8px rgba(0,0,0,.2);
  }
  .circle-photo--skin { left: 50px; top: 140px; width: 190px; height: 190px;
    background: radial-gradient(circle at 45% 40%, #f1d6c6, #cfa48d); }
  .circle-photo--nails { left: 215px; top: 160px; width: 170px; height: 170px;
    background: radial-gradient(circle at 50% 45%, #e7b3b1, #9c3f55); }
  .front-wave { position: absolute; left: 0; top: 300px; width: 820px; height: 100px; }
  .tagline {
    position: absolute; left: 40px; top: 395px; width: 400px;
    font-family: "Berkshire Swash", serif; font-size: 38px; line-height: 1.2; color: var(--brown);
  }
  .services {
    position: absolute; right: 0; bottom: 0; width: 360px; height: 185px;
    background: var(--tan); padding: 22px 26px; list-style: none;
    font-family: "Oswald", sans-serif; color: #fff;
  }
  .services li { position: relative; padding-left: 18px; font-size: 18px; line-height: 1.45; }
  .services li.minor { font-size: 15px; font-family: "Open Sans", sans-serif; }
  .services li::before {
    content: ""; position: absolute; left: 0; top: 50%; width: 8px; height: 8px;
    margin-top: -4px; border-radius: 50%; background: #fff;
  }

  /* Back */
  .message-panel {
    position: absolute; left: 0; top: 0; width: 410px; height: 540px;
    background: linear-gradient(160deg, var(--pink-soft), var(--pink) 55%, var(--pink-deep));
  }
  .figure-art {
    position: absolute; left: 30px; top: 25px; width: 150px; height: 170px;
    border-radius: 50% 40% 50% 40%;
    background: linear-gradient(160deg, rgba(255,255,255,.7), rgba(228,142,160,.6));
  }
  .back-title {
    position: absolute; left: 34px; top: 205px;
    font-family: "Oswald", sans-serif; font-weight: 600; font-size: 34px; color: #fff;
  }
  .back-subtitle {
    position: absolute; left: 60px; top: 256px;
    font-family: "Oswald", sans-serif; font-size: 18px; color: #fbe9ec;
  }
  .back-body {
    position: absolute; left: 34px; top: 292px; width: 340px;
    font-family: "Open Sans", sans-serif; font-weight: 600; font-size: 19px;
    line-height: 1.3; color: var(--ink);
  }
  .back-wave { position: absolute; left: 0; top: 400px; width: 410px; height: 80px; }
  .circle-photo--hair { left: 130px; top: 405px; width: 130px; height: 130px;
    background: radial-gradient(circle at 50% 40%, #c89478, #5a3322); }

  .clinic-info {
    position: absolute; left: 450px; top: 0; width: 340px; height: 540px;
    display: flex; flex-direction: column; justify-content: center; gap: 22px;
  }
  .clinic-name {
    font-family: "Oswald", sans-serif; font-weight: 600; font-size: 30px;
    line-height: 1.15; color: var(--brown);
  }
  .clinic-name span {
    display: block; font-weight: 400; font-size: 18px; color: var(--orange);
    text-transform: uppercase; letter-spacing: .5px; margin-top: 4px;
  }
  .clinic-rule { width: 80px; height: 4px; background: var(--pink-deep); }
  .contact-line {
    display: flex; align-items: flex-start; gap: 12px;
    font-size: 18px; line-height: 1.35; color: var(--ink);
  }
  .contact-line svg { flex: none; width: 22px; height: 22px; margin-top: 2px; }
  .contact-line--phone { font-family: "Oswald", sans-serif; font-size: 26px; font-weight: 500; color: var(--brown); }
  .insurance-note {
    background: var(--pink-soft); border-left: 5px solid var(--pink-deep);
    padding: 12px 16px; font-size: 16px; font-weight: 600; line-height: 1.35; color: var(--ink);
  }
</style>
</head>
<body>

<section class="postcard postcard--front">
  <div class="hero-photo" role="img" aria-label="Portrait photo of a woman with clear skin"></div>
  <h1 class="headline">Dermatology services adding care for skin, hair and nails</h1>
  <svg class="front-wave" viewBox="0 0 820 100" preserveAspectRatio="none" aria-hidden="true">
    <path d="M0 60 C200 10 420 90 820 20 L820 100 L0 100 Z" fill="#f8dde2"/>
    <path d="M0 70 C220 20 430 100 820 35" fill="none" stroke="#e48ea0" stroke-width="6"/>
  </svg>
  <div class="circle-photo circle-photo--skin" role="img" aria-label="Close-up photo of facial skin"></div>
  <div class="circle-photo circle-photo--nails" role="img" aria-label="Photo of manicured nails"></div>
  <p class="tagline">Dermatologist now in Wauchula, Florida</p>
  <ul class="services">
    <li>Skin exams</li>
    <li class="minor">Skin Disorders</li>
    <li>Skin Biopsies</li>
    <li class="minor">Mole and Skin Tag removed</li>
    <li>Treatment of various skin</li>
    <li class="minor">Hair and nail disease</li>
  </ul>
</section>

<section class="postcard postcard--back">
  <div class="message-panel">
    <div class="figure-art" role="img" aria-label="Decorative illustration of a woman's silhouette"></div>
    <h2 class="back-title">No need to drive</h2>
    <p class="back-subtitle">Care in your community</p>
    <p class="back-body">Treat skin problems like skin cancers, rosacea, psoriasis, eczema, wound care and other breakdowns</p>
    <svg class="back-wave" viewBox="0 0 410 80" preserveAspectRatio="none" aria-hidden="true">
      <path d="M0 40 C120 10 260 70 410 30" fill="none" stroke="#ffffff" stroke-width="4"/>
      <path d="M0 52 C130 24 270 80 410 44" fill="none" stroke="#e48ea0" stroke-width="4"/>
    </svg>
    <div class="circle-photo circle-photo--hair" role="img" aria-label="Photo of a woman with long healthy hair"></div>
  </div>

  <div class="clinic-info">
    <h3 class="clinic-name">Marlow Tenbury Inc<span>Expanding its services</span></h3>
    <div class="clinic-rule"></div>
    <p class="contact-line">
      <svg viewBox="0 0 24 24" aria-hidden="true"><path d="M12 2a7 7 0 0 0-7 7c0 5 7 13 7 13s7-8 7-13a7 7 0 0 0-7-7zm0 9.5A2.5 2.5 0 1 1 12 6.5a2.5 2.5 0 0 1 0 5z" fill="#e48ea0"/></svg>
      <span>482 N Larkin Avenue<br>Wauchula, Florida 33870</span>
    </p>
    <p class="contact-line contact-line--phone">
      <svg viewBox="0 0 24 24" aria-hidden="true"><path d="M6.6 10.8a15 15 0 0 0 6.6 6.6l2.2-2.2a1 1 0 0 1 1-.25 11.4 11.4 0 0 0 3.6.57 1 1 0 0 1 1 1V20a1 1 0 0 1-1 1A17 17 0 0 1 3 4a1 1 0 0 1 1-1h3.5a1 1 0 0 1 1 1c0 1.25.2 2.45.57 3.6a1 1 0 0 1-.25 1z" fill="#e48ea0"/></svg>
      <span>863-555-0182</span>
    </p>
    <p class="insurance-note">Most insurance accepted including Medicare</p>
  </div>
</section>

</body>
</html>
```